Spring potato equipment ad in line with past design done for company

Create new flyer ad for spring, summer season for potato equipment. I will be using this ad in electronic format, social media and print ad in magazines. Looking for something to help promote our potato equipment (bulk box and piler) I have attached 3 photos, one of the piler alone, the other of the box on a truck (the way they work) and the other is both in the yard here. I can look for other photos of the equipment if this helps. I have included the insert ad, this is what we use on one of the equipment ads, looking for something versatile like this ad.
Farmers
Agricultural industry

```html
<!DOCTYPE html>
<html lang="en">
<head>
<meta charset="utf-8">
<title>Kestrel Group – Spring Potato Equipment Flyers</title>
<link href="https://fonts.googleapis.com/css2?family=Lato:ital,wght@0,400;0,700;0,900;1,400;1,700;1,900&display=swap" rel="stylesheet">
<style>
  :root {
    --ink: #0b0b0b;
    --red: #ec1c24;
    --white: #ffffff;
    --paper: #ffffff;
    --photo-dark: #1a1a1a;
    --photo-mid: #8a8a8a;
    --photo-light: #c9c9c9;
  }
  * { box-sizing: border-box; margin: 0; padding: 0; }
  html, body { width: 1200px; height: 900px; overflow: hidden; background: var(--paper); }
  body { position: relative; font-family: "Lato", sans-serif; color: var(--white); }

  .flyer {
    position: absolute; top: 203px; width: 352px; height: 458px;
    background: var(--ink); overflow: hidden;
    box-shadow: 4px 5px 7px rgba(0,0,0,.45);
  }
  .flyer--banner { left: 49px; }
  .flyer--hex { left: 425px; }
  .flyer--wave { left: 799px; }

  .brand {
    display: flex; align-items: center; gap: 7px;
    font-weight: 900; font-size: 20px; letter-spacing: .5px; color: var(--white);
    line-height: 1;
  }
  .brand__dot { width: 12px; height: 12px; border-radius: 50%; background: var(--red); flex: none; }

  .header { position: absolute; left: 0; top: 0; width: 100%; height: 61px;
    display: flex; justify-content: center; align-items: center; background: var(--ink); }
  .contact-bar { position: absolute; left: 0; top: 61px; width: 100%; height: 19px;
    background: var(--red); font-size: 7.5px; font-weight: 700;
    display: flex; justify-content: center; align-items: center; }

  .photo { position: absolute; }
  .flyer--banner .photo {
    left: 0; top: 80px; width: 100%; height: 365px;
    background: linear-gradient(180deg, var(--photo-dark) 0%, #555 22%, var(--photo-mid) 40%, var(--photo-light) 62%, #9a9a9a 78%, var(--photo-dark) 100%);
  }
  .tagline { position: absolute; left: 0; width: 100%; text-align: center;
    font-style: italic; font-size: 9.5px; line-height: 1; }
  .tagline strong { font-weight: 900; }
  .flyer--banner .tagline { top: 411px; }
  .foot-bar { position: absolute; left: 0; bottom: 0; width: 100%; height: 12px; background: var(--red); }

  .flyer--hex .shapes { position: absolute; inset: 0; width: 100%; height: 100%; }
  .flyer--hex .brand { position: absolute; left: 23px; top: 22px; }
  .flyer--hex .phone { position: absolute; left: 24px; top: 76px; font-size: 12px; font-weight: 700; font-style: italic; }
  .flyer--hex .web { position: absolute; left: 24px; top: 92px; font-size: 7px; }
  .pitch { position: absolute; left: 21px; top: 158px; width: 120px; font-size: 12px; line-height: 15.3px; }
  .pitch strong { display: block; font-weight: 900; font-style: italic; font-size: 15px; line-height: 19.5px; }
  .pitch strong span { font-weight: 900; }
  .pitch-rule { position: absolute; left: 21px; top: 338px; width: 64px; height: 4px; background: var(--red); }

  .flyer--wave .photo {
    left: 0; top: 80px; width: 100%; height: 300px;
    background: linear-gradient(180deg, var(--photo-dark) 0%, #5a5a5a 20%, var(--photo-mid) 40%, var(--photo-light) 65%, #a5a5a5 100%);
  }
  .flyer--wave .shapes { position: absolute; inset: 0; width: 100%; height: 100%; }
  .flyer--wave .tagline { top: 422px; }
</style>
</head>
<body>

  <!-- Flyer 1: banner header -->
  <section class="flyer flyer--banner">
    <div class="header"><div class="brand"><span class="brand__dot"></span>KESTREL GROUP</div></div>
    <div class="contact-bar">1(800) 555-0148 | kestrelagriculture.com</div>
    <div class="photo" role="img" aria-label="Black and white photo of a potato piler conveyor in a gravel yard with a bulk box truck in the foreground"></div>
    <p class="tagline"><strong>Upgrade your game</strong> to out top-of-the-line equipment, whether you<br>are looking for a piler, bulk box or insert, we have you covered.</p>
    <div class="foot-bar"></div>
  </section>

  <!-- Flyer 2: hexagon window -->
  <section class="flyer flyer--hex">
    <svg class="shapes" viewBox="0 0 376 488" preserveAspectRatio="none" aria-hidden="true">
      <defs>
        <linearGradient id="hexPhoto" x1="0" y1="0" x2="0" y2="1">
          <stop offset="0" stop-color="#d8d8d8"/>
          <stop offset=".3" stop-color="#6a6a6a"/>
          <stop offset=".55" stop-color="#b5b5b5"/>
          <stop offset=".75" stop-color="#8c8c8c"/>
          <stop offset="1" stop-color="#c4c4c4"/>
        </linearGradient>
      </defs>
      <rect x="248" y="0" width="105" height="488" fill="#ec1c24"/>
      <polygon points="0,372 118,488 0,488" fill="#ec1c24"/>
      <polygon points="247,48 345,103 345,393 247,448 153,393 153,103" fill="#0b0b0b" transform="translate(3,3)" opacity=".6"/>
      <polygon points="247,48 345,103 345,393 247,448 153,393 153,103" fill="url(#hexPhoto)" role="img" aria-label="Black and white photo of the piler and bulk box truck in the yard"/>
    </svg>
    <div class="brand"><span class="brand__dot"></span>KESTREL GROUP</div>
    <p class="phone">1(800) 555-0148</p>
    <p class="web">kestrelagriculture.com</p>
    <p class="pitch"><strong>Upgrade your game to out top-of-the-line equipment<span style="font-style:normal">,</span></strong>whether you are looking for a piler, bulk box or insert, we have you covered.</p>
    <div class="pitch-rule"></div>
  </section>

  <!-- Flyer 3: red wave -->
  <section class="flyer flyer--wave">
    <div class="header"><div class="brand"><span class="brand__dot"></span>KESTREL GROUP</div></div>
    <div class="contact-bar">1(800) 555-0148 | kestrelagriculture.com</div>
    <div class="photo" role="img" aria-label="Black and white photo of a potato piler conveyor behind a bulk box mounted on a truck"></div>
    <svg class="shapes" viewBox="0 0 376 488" preserveAspectRatio="none" aria-hidden="true">
      <path d="M0,330 Q200,380 376,300 L376,488 L0,488 Z" fill="#0b0b0b"/>
      <path d="M0,330 Q200,380 376,300 L376,340 Q230,440 0,425 Z" fill="#ec1c24"/>
      <path d="M0,398 Q220,408 376,318" fill="none" stroke="#ffffff" stroke-width="1.3"/>
    </svg>
    <p class="tagline"><strong>Upgrade your game</strong> to out top-of-the-line equipment, whether you<br>are looking for a piler, bulk box or insert, we have you covered.</p>
  </section>

</body>
</html>
```